Simple and Approachable Cover for Pet Expo Company Page

Size: 2000 x 430; looking simply for words "Dunmore HR Consulting" and email address "DunmoreHRConsulting@brelvamail.com." This is for a cover photo for a company profile page for the Hollow Oak Expo, where I am a featured speaker on Employee Communications later this month. You can incorporate the attached photo to the left of the banner ad if you wish. The mood I wish to present is approachable, positive and simple.

Target Market(s)

small pet retail business owners

Industry/Entity Type

Pet Shop

Font styles to use
Serif
Sans Serif

Requirements
Must have
• Email address clearly defined/separated. Easy to read.
Nice to have
• I like the picture that I included; subtle pet paw background is also nice
Should not have
• No paid stock images

```html
<!DOCTYPE html>
<html lang="en">
<head>
<meta charset="utf-8">
<title>Dunmore HR Consulting – Cover Banner</title>
<link href="https://fonts.googleapis.com/css2?family=Abhaya+Libre:wght@800&family=Open+Sans:wght@400&display=swap" rel="stylesheet">
<style>
  :root {
    --page: #f4f7f8;
    --frame: #ffffff;
    --panel: #e2e2e2;
    --bubble: #ffffff;
    --ink: #151515;
    --cat-light: #b9a58e;
    --cat-dark: #4a3a2c;
    --dog-light: #b0521f;
    --dog-dark: #6e2a0e;
  }
  html, body {
    margin: 0;
    padding: 0;
    width: 1200px;
    height: 1000px;
    overflow: hidden;
    background: var(--page);
  }
  .canvas {
    position: relative;
    width: 1200px;
    height: 1000px;
  }
  .banner {
    position: absolute;
    left: 25px;
    top: 367px;
    width: 1151px;
    height: 265px;
    background: var(--frame);
    box-shadow: 0 6px 22px rgba(0, 0, 0, 0.35);
  }
  .banner-panel {
    position: absolute;
    left: 24px;
    top: 21px;
    width: 1105px;
    height: 222px;
    background: var(--panel);
    overflow: hidden;
  }
  .pet-photo {
    position: absolute;
    bottom: 0;
  }
  .pet-photo--cat {
    left: 0;
    width: 182px;
    height: 165px;
    background: radial-gradient(ellipse at 60% 45%, var(--cat-light), var(--cat-dark) 80%);
    border-radius: 50% 50% 0 0 / 40% 40% 0 0;
  }
  .pet-photo--dog {
    left: 841px;
    width: 246px;
    height: 207px;
    background: radial-gradient(ellipse at 55% 40%, var(--dog-light), var(--dog-dark) 85%);
    border-radius: 45% 50% 0 0 / 40% 45% 0 0;
  }
  .bubbles {
    position: absolute;
    left: 0;
    top: 0;
  }
  .bubble-text {
    position: absolute;
    margin: 0;
    color: var(--ink);
    text-align: center;
    white-space: nowrap;
  }
  .company-name {
    left: 211px;
    top: 45px;
    width: 630px;
    font-family: "Abhaya Libre", Georgia, serif;
    font-weight: 800;
    font-size: 38px;
    letter-spacing: 0.5px;
    line-height: 1;
  }
  .company-email {
    left: 243px;
    top: 150px;
    width: 625px;
    font-family: "Open Sans", Arial, sans-serif;
    font-weight: 400;
    font-size: 24px;
    line-height: 1;
  }
</style>
</head>
<body>
<main class="canvas">
  <section class="banner">
    <div class="banner-panel">
      <div class="pet-photo pet-photo--cat" role="img" aria-label="Photo of a tabby kitten looking to the right"></div>
      <div class="pet-photo pet-photo--dog" role="img" aria-label="Photo of a red setter dog with a white collar looking to the left"></div>

      <svg class="bubbles" width="1105" height="222" viewBox="0 0 1105 222" aria-hidden="true">
        <defs>
          <filter id="bubble-shadow" x="-10%" y="-30%" width="120%" height="160%">
            <feDropShadow dx="1" dy="3" stdDeviation="2.5" flood-color="#000" flood-opacity="0.35"/>
          </filter>
        </defs>
        <g filter="url(#bubble-shadow)" fill="var(--bubble)">
          <path class="speech-bubble speech-bubble--name"
                d="M 524 20 C 350 20 212 40 212 63 C 212 86 350 108 524 108 C 640 108 740 100 790 92 L 841 92 L 805 84 C 830 78 838 70 838 63 C 838 40 700 20 524 20 Z"/>
          <path class="speech-bubble speech-bubble--email"
                d="M 555 120 C 382 120 244 140 244 165 C 244 176 255 185 270 192 L 222 194 L 290 200 C 340 208 440 212 555 212 C 728 212 866 190 866 165 C 866 140 728 120 555 120 Z"/>
        </g>
      </svg>

      <h1 class="bubble-text company-name">Dunmore HR Consulting</h1>
      <p class="bubble-text company-email">DunmoreHRConsulting@brelvamail.com</p>
    </div>
  </section>
</main>
</body>
</html>
```